Real Estate Development Company Stationary

We need our company, business card, letterhead, pocket folder and envelope designed.

We are a new real estate development company. We focus on data centre, commercial and real estate development.

Please see attached for our logo. Since it's a new logo, you still can make minor adjust if you like it makes senses

The client has sent me a business card he really likes. Please see file 3.

Target Market(s)

Real Estate Investors
Large corporations
Home buyers

Industry/Entity Type

Real Estate

```html
<!DOCTYPE html>
<html lang="en">
<head>
<meta charset="utf-8">
<title>Kestrel Development Inc. – Stationery</title>
<link rel="stylesheet" href="https://fonts.googleapis.com/css2?family=Open+Sans:wght@400;600;700&family=Comfortaa:wght@400&family=Great+Vibes&display=swap">
<style>
  :root {
    --bg: #d3d3d3;
    --paper: #f7f7f7;
    --navy: #1b3f73;
    --green: #5e9a2c;
    --green-light: #6aa636;
    --ink: #4a4a4a;
    --muted: #8a8a8a;
  }
  * { box-sizing: border-box; margin: 0; padding: 0; }
  html, body { width: 1200px; height: 800px; overflow: hidden; }
  body {
    background: radial-gradient(ellipse at 70% 20%, #e0e0e0 0%, var(--bg) 60%, #c8c8c8 100%);
    font-family: "Open Sans", Arial, sans-serif;
    position: relative;
  }
  .item { position: absolute; }

  /* brand name lockup */
  .brand { display: flex; align-items: center; gap: 4px; color: var(--green);
    font-family: "Comfortaa", "Open Sans", sans-serif; font-weight: 400; white-space: nowrap; }
  .brand .mark { background: var(--green); flex: none; }

  /* letterhead */
  .letterhead { left: 259px; top: 87px; width: 208px; height: 295px; background: var(--paper); padding: 14px 14px 0 14px; }
  .letterhead .brand { font-size: 9px; }
  .letterhead .brand .mark { width: 7px; height: 7px; }
  .letter-body { position: absolute; left: 24px; top: 74px; width: 169px; font-size: 3.6px; line-height: 5.4px; color: var(--ink); }
  .letter-body .salutation { font-weight: 700; margin-bottom: 5px; }
  .letter-body p { margin-bottom: 4px; }
  .signature { margin-top: 24px; }
  .signature .script { font-family: "Great Vibes", cursive; font-size: 10px; color: #333; line-height: 10px; }
  .signature .role { font-size: 3.8px; font-weight: 600; color: #333; }
  .letter-footer { position: absolute; left: 14px; right: 14px; bottom: 8px; display: flex;
    justify-content: space-between; font-size: 3.4px; line-height: 4.6px; color: var(--ink); }
  .letter-footer .col { padding-left: 6px; border-left: 0.6px solid #999; }
  .letter-footer .col:first-child { border-left: none; padding-left: 0; }
  .letter-footer .web { color: var(--green); }

  /* open envelope */
  .envelope-open { left: 498px; top: 128px; width: 219px; height: 149px; }
  .envelope-open svg { display: block; }

  /* envelope front */
  .envelope-front { left: 742px; top: 128px; width: 218px; height: 109px; background: var(--paper); padding: 9px 9px; }
  .envelope-front .brand { font-size: 9px; }
  .envelope-front .brand .mark { width: 6px; height: 6px; }
  .envelope-front .return { position: absolute; left: 9px; bottom: 6px; font-size: 3px; line-height: 3.8px; color: var(--ink); }

  /* envelope back */
  .envelope-back { left: 742px; top: 268px; width: 219px; height: 110px; background: var(--paper); overflow: hidden; }
  .envelope-back svg { position: absolute; left: 0; top: 0; }
  .envelope-back .url { position: absolute; left: 92px; top: 18px; font-size: 3.4px; color: #fff; letter-spacing: 0.1px; }

  /* folder cover */
  .folder-cover { left: 241px; top: 412px; width: 228px; height: 306px; background: var(--navy);
    box-shadow: 1px 2px 3px rgba(0,0,0,0.18); }
  .folder-cover .brand { position: absolute; left: 0; right: 0; top: 254px; justify-content: center; font-size: 22px; gap: 7px; }
  .folder-cover .brand .mark { width: 14px; height: 14px; }

  /* open folder */
  .folder-open { left: 501px; top: 409px; width: 456px; height: 304px; }
  .folder-open svg { display: block; }
</style>
</head>
<body>

  <!-- Letterhead -->
  <section class="item letterhead">
    <div class="brand"><span class="mark"></span><span>Kestrel Development</span></div>
    <div class="letter-body">
      <p class="salutation">Dear Partner,</p>
      <p>Thank you for your interest in our latest projects. We plan, build and manage modern spaces for companies, investors and families across the region, with a clear focus on quality, long term value and careful use of land. Every site we take on is chosen with care and developed with partners we trust and know well.</p>
      <p>Our team brings long experience in data centres, offices and homes. We work closely with each client from the first sketch to the final handover, and we keep you informed at every step along the way.</p>
      <p>Please find enclosed a short overview of our current sites, the planned phases and the key dates for the coming year. It also lists the main contacts for each project, so that you can reach the right person quickly whenever a question comes up during planning or construction.</p>
      <p>We would be glad to meet with you in person and discuss how we can support your plans, whether you are looking for a new office, a secure data hall or a family home.</p>
      <p>Should you need any further details in the meantime, do not hesitate to call or write to us. We look forward to hearing from you and to building something lasting together. With kind regards from all of us at the office.</p>
      <div class="signature">
        <div class="script">Your Name</div>
        <div class="role">Company Director</div>
      </div>
    </div>
    <footer class="letter-footer">
      <div class="col">t. +41 41 000 12 34<br>m. +41 79 000 56 78</div>
      <div class="col">Lindenweg 8, 6300 Zug<br>Switzerland</div>
      <div class="col">office@kestreldev.com<br><span class="web">www.kestreldev.com</span></div>
    </footer>
  </section>

  <!-- Open envelope with green flap -->
  <div class="item envelope-open">
    <svg width="219" height="149" viewBox="0 0 219 149">
      <path d="M4 40 L4 5 Q4 0 10 0 L209 0 Q215 0 215 5 L215 40 Z" fill="var(--green)"/>
      <rect x="0" y="39" width="219" height="110" fill="var(--paper)"/>
      <path d="M14 39 L14 62 Q14 66 18 66 L201 66 Q205 66 205 62 L205 39" fill="none" stroke="#dcdcdc" stroke-width="0.8"/>
      <path d="M0 148.5 L219 148.5" stroke="#cfcfcf" stroke-width="1"/>
    </svg>
  </div>

  <!-- Envelope front -->
  <section class="item envelope-front">
    <div class="brand"><span class="mark"></span><span>Kestrel</span></div>
    <div class="return">Lindenweg 8, 6300 Zug<br>Switzerland</div>
  </section>

  <!-- Envelope back with navy flap -->
  <section class="item envelope-back">
    <svg width="219" height="110" viewBox="0 0 219 110">
      <path d="M0 0 L219 0 L219 4 L214 42 L4 42 Q0 42 0 38 Z" fill="var(--navy)"/>
      <path d="M4 42 L214 42" stroke="#c9c9c9" stroke-width="0.8"/>
    </svg>
    <span class="url">www.kestreldev.com</span>
  </section>

  <!-- Pocket folder cover -->
  <section class="item folder-cover">
    <div class="brand"><span class="mark"></span><span>Kestrel</span></div>
  </section>

  <!-- Pocket folder open -->
  <div class="item folder-open">
    <svg width="456" height="304" viewBox="0 0 456 304">
      <defs>
        <linearGradient id="leftPanel" x1="0" y1="0" x2="1" y2="0">
          <stop offset="0" stop-color="#f3f3f3"/><stop offset="1" stop-color="#e9e9e9"/>
        </linearGradient>
        <linearGradient id="rightPanel" x1="0" y1="0" x2="1" y2="0">
          <stop offset="0" stop-color="#e6e6e6"/><stop offset="1" stop-color="#f2f2f2"/>
        </linearGradient>
      </defs>
      <rect x="0" y="0" width="228" height="304" fill="url(#leftPanel)"/>
      <rect x="228" y="0" width="228" height="304" fill="url(#rightPanel)"/>
      <line x1="228" y1="0" x2="228" y2="304" stroke="#d8d8d8" stroke-width="1"/>
      <path d="M0 204 L204 204 Q214 204 214 214 L223 304 L0 304 Z" fill="var(--green)"/>
      <path d="M456 204 L252 204 Q242 204 241 214 L232 304 L456 304 Z" fill="var(--green-light)"/>
    </svg>
  </div>

</body>
</html>
```